Dental Medical History Form - Content provided

Design a medical history form for a dental practice. Content is provided so all that is needed is the formatting to make it look great and easy to read.

"Patient Information" to include all information contained in top portion of the "Patient Medical History Form" docx file.

"Medical History" should follow the formatting and content of the "Exact Medical History" file as this is what the entry fields look like in our practice software and so we would like it to match.

1st page - Patient info, allergies, medications, antibiotics, joint replacement, pregnancy.

2nd page - Do you have, or have you had, any of the following? . . . . . . .
Updates

Target Market(s)

All ages but must be clear enough for elderly to read. Use as much space as possible to keep font size bigger yet keep to two pages

Industry/Entity Type

Dental

Font styles to use
Sans Serif

Requirements
Must have
• All content provided
• Our logo at the top (file provided)
• Century Gothic Font
• Limit to two pages

```html
<!DOCTYPE html>
<html lang="en">
<head>
<meta charset="utf-8">
<title>Lumen Dental – Medical History</title>
<link href="https://fonts.googleapis.com/css2?family=Questrial&family=Mulish:wght@700&display=swap" rel="stylesheet">
<style>
  :root{
    --ink:#3a3a3c;
    --text:#5a5a5c;
    --rule:#b9b9bb;
    --band:#58585b;
    --paper:#ffffff;
    --row:18.56px;
  }
  *{box-sizing:border-box;margin:0;padding:0}
  html,body{width:848px;height:1200px;overflow:hidden;background:var(--paper)}
  body{position:relative;font-family:"Questrial",sans-serif;color:var(--text)}
  .brand{position:absolute;left:51px;top:84px;color:var(--band);font-family:"Questrial",sans-serif;font-size:30px;line-height:1;letter-spacing:0.5px}
  .contact{position:absolute;left:612px;top:56px;font-family:"Mulish",sans-serif;font-weight:700;font-size:12.4px;color:var(--ink);line-height:15.5px}
  .contact .gap{margin-top:4.5px}
  .header-rule{position:absolute;left:0;top:145px}
  .form-frame{position:absolute;left:46px;top:173px;width:756px;height:915px;border:1px solid var(--rule)}
  .question{position:absolute;left:51px;top:183px;font-family:"Mulish",sans-serif;font-weight:700;font-size:12.4px;color:var(--ink)}
  .column{position:absolute;top:213.3px;display:flex;flex-direction:column}
  .col-left{left:51px;width:352px}
  .col-right{left:429px;width:350px}
  .row{height:var(--row);display:flex;align-items:center;font-size:13.4px;white-space:nowrap}
  .col-left .label{flex:0 0 263px}
  .col-right .label{flex:0 0 261px}
  .section-title{font-family:"Mulish",sans-serif;font-weight:700;font-size:12.6px;color:var(--ink);text-decoration:underline;text-underline-offset:2px}
  .options{display:flex;align-items:center;font-size:13px}
  .opt{display:flex;align-items:center;width:48px}
  .opt span{width:24px}
  .tick-box{width:16.5px;height:16.5px;border:1.2px solid #2e2e30;border-radius:50%;display:inline-block}
  .other-line{position:absolute;left:429px;top:975px;width:369px;display:flex;align-items:flex-end;font-family:"Mulish",sans-serif;font-weight:700;font-size:12.4px;color:var(--ink)}
  .sign-line{position:absolute;top:1058px;display:flex;align-items:flex-end;font-family:"Mulish",sans-serif;font-weight:700;font-size:12.4px;color:var(--ink)}
  .sign-line.signature{left:51px;width:333px}
  .sign-line.date{left:429px;width:369px}
  .fill{flex:1;border-bottom:1px solid var(--ink);margin-left:1px;height:12px}
  .footer{position:absolute;left:0;top:1102px;width:848px;height:98px;background:var(--band);color:#fff;font-style:italic;font-size:12.2px;text-align:center;padding-top:16px;line-height:14.5px}
</style>
</head>
<body>
  <div class="brand">Lumen Dental</div>

  <div class="contact">
    <div>4.05/118 Coastal Parade</div>
    <div>Northaven NSW 2260</div>
    <div class="gap">(02) 5550 1234</div>
    <div class="gap">www.lumendental.com.au</div>
  </div>

  <svg class="header-rule" width="848" height="10" viewBox="0 0 848 10" aria-hidden="true">
    <polygon points="0,1 292,1 300,8 0,8" fill="#58585b"/>
    <rect x="0" y="7" width="848" height="1.3" fill="#58585b"/>
  </svg>

  <div class="form-frame"></div>
  <p class="question">Do you have, or have you had, any of the following?</p>

  <div class="column col-left">
    <div class="row"><span class="section-title">Dental</span></div>
    <div class="row"><span class="label">Acid Reflux</span><span class="options"><span class="opt"><span>Yes</span><i class="tick-box"></i></span><span class="opt"><span>No</span><i class="tick-box"></i></span></span></div>
    <div class="row"><span class="label">Bad Breath/Taste</span><span class="options"><span class="opt"><span>Yes</span><i class="tick-box"></i></span><span class="opt"><span>No</span><i class="tick-box"></i></span></span></div>
    <div class="row"><span class="label">Bleeding/Swollen/Sore Gums</span><span class="options"><span class="opt"><span>Yes</span><i class="tick-box"></i></span><span class="opt"><span>No</span><i class="tick-box"></i></span></span></div>
    <div class="row"><span class="label">Blisters/Ulcers in Mouth</span><span class="options"><span class="opt"><span>Yes</span><i class="tick-box"></i></span><span class="opt"><span>No</span><i class="tick-box"></i></span></span></div>
    <div class="row"><span class="label">Broken tooth/filling</span><span class="options"><span class="opt"><span>Yes</span><i class="tick-box"></i></span><span class="opt"><span>No</span><i class="tick-box"></i></span></span></div>
    <div class="row"><span class="label">Burning tongue</span><span class="options"><span class="opt"><span>Yes</span><i class="tick-box"></i></span><span class="opt"><span>No</span><i class="tick-box"></i></span></span></div>
    <div class="row"><span class="label">Dry mouth</span><span class="options"><span class="opt"><span>Yes</span><i class="tick-box"></i></span><span class="opt"><span>No</span><i class="tick-box"></i></span></span></div>
    <div class="row"><span class="label">Food collection between teeth</span><span class="options"><span class="opt"><span>Yes</span><i class="tick-box"></i></span><span class="opt"><span>No</span><i class="tick-box"></i></span></span></div>
    <div class="row"><span class="label">Grinding/clenching teeth (day/night)</span><span class="options"><span class="opt"><span>Yes</span><i class="tick-box"></i></span><span class="opt"><span>No</span><i class="tick-box"></i></span></span></div>
    <div class="row"><span class="label">Loose teeth</span><span class="options"><span class="opt"><span>Yes</span><i class="tick-box"></i></span><span class="opt"><span>No</span><i class="tick-box"></i></span></span></div>
    <div class="row"><span class="label">Crooked teeth</span><span class="options"><span class="opt"><span>Yes</span><i class="tick-box"></i></span><span class="opt"><span>No</span><i class="tick-box"></i></span></span></div>
    <div class="row"><span class="label">Discoloured teeth</span><span class="options"><span class="opt"><span>Yes</span><i class="tick-box"></i></span><span class="opt"><span>No</span><i class="tick-box"></i></span></span></div>
    <div class="row"><span class="label">Sensitivity to Hot/Cold</span><span class="options"><span class="opt"><span>Yes</span><i class="tick-box"></i></span><span class="opt"><span>No</span><i class="tick-box"></i></span></span></div>
    <div class="row"><span class="label">Tooth pain when chewing</span><span class="options"><span class="opt"><span>Yes</span><i class="tick-box"></i></span><span class="opt"><span>No</span><i class="tick-box"></i></span></span></div>
    <div class="row"><span class="label">Jaw pain/Fracture</span><span class="options"><span class="opt"><span>Yes</span><i class="tick-box"></i></span><span class="opt"><span>No</span><i class="tick-box"></i></span></span></div>
    <div class="row"><span class="label">Orthodontic treatment/history</span><span class="options"><span class="opt"><span>Yes</span><i class="tick-box"></i></span><span class="opt"><span>No</span><i class="tick-box"></i></span></span></div>
    <div class="row"><span class="label">Oral Cancer</span><span class="options"><span class="opt"><span>Yes</span><i class="tick-box"></i></span><span class="opt"><span>No</span><i class="tick-box"></i></span></span></div>
    <div class="row"></div>
    <div class="row"><span class="section-title">Diet/Lifestyle&nbsp;&nbsp;&nbsp;</span></div>
    <div class="row"><span class="label">Drink more than one glass alcohol per day</span><span class="options"><span class="opt"><span>Yes</span><i class="tick-box"></i></span><span class="opt"><span>No</span><i class="tick-box"></i></span></span></div>
    <div class="row"><span class="label">Smoking</span><span class="options"><span class="opt"><span>Yes</span><i class="tick-box"></i></span><span class="opt"><span>No</span><i class="tick-box"></i></span></span></div>
    <div class="row"><span class="label">Carbonated drinks</span><span class="options"><span class="opt"><span>Yes</span><i class="tick-box"></i></span><span class="opt"><span>No</span><i class="tick-box"></i></span></span></div>
    <div class="row"><span class="label">Sugary foods</span><span class="options"><span class="opt"><span>Yes</span><i class="tick-box"></i></span><span class="opt"><span>No</span><i class="tick-box"></i></span></span></div>
    <div class="row"></div>
    <div class="row"><span class="section-title">Blood</span></div>
    <div class="row"><span class="label">Anaemia</span><span class="options"><span class="opt"><span>Yes</span><i class="tick-box"></i></span><span class="opt"><span>No</span><i class="tick-box"></i></span></span></div>
    <div class="row"><span class="label">Blood clots</span><span class="options"><span class="opt"><span>Yes</span><i class="tick-box"></i></span><span class="opt"><span>No</span><i class="tick-box"></i></span></span></div>
    <div class="row"><span class="label">Leukemia</span><span class="options"><span class="opt"><span>Yes</span><i class="tick-box"></i></span><span class="opt"><span>No</span><i class="tick-box"></i></span></span></div>
    <div class="row"><span class="label">Low platelets</span><span class="options"><span class="opt"><span>Yes</span><i class="tick-box"></i></span><span class="opt"><span>No</span><i class="tick-box"></i></span></span></div>
    <div class="row"><span class="label">Lymphoma</span><span class="options"><span class="opt"><span>Yes</span><i class="tick-box"></i></span><span class="opt"><span>No</span><i class="tick-box"></i></span></span></div>
    <div class="row"><span class="label">Haemophelia</span><span class="options"><span class="opt"><span>Yes</span><i class="tick-box"></i></span><span class="opt"><span>No</span><i class="tick-box"></i></span></span></div>
    <div class="row"></div>
    <div class="row"><span class="section-title">Chest</span></div>
    <div class="row"><span class="label">Bronchitis</span><span class="options"><span class="opt"><span>Yes</span><i class="tick-box"></i></span><span class="opt"><span>No</span><i class="tick-box"></i></span></span></div>
    <div class="row"><span class="label">Cystic Fibrosis</span><span class="options"><span class="opt"><span>Yes</span><i class="tick-box"></i></span><span class="opt"><span>No</span><i class="tick-box"></i></span></span></div>
    <div class="row"><span class="label">Emphysema</span><span class="options"><span class="opt"><span>Yes</span><i class="tick-box"></i></span><span class="opt"><span>No</span><i class="tick-box"></i></span></span></div>
    <div class="row"><span class="label">Pneumonia</span><span class="options"><span class="opt"><span>Yes</span><i class="tick-box"></i></span><span class="opt"><span>No</span><i class="tick-box"></i></span></span></div>
    <div class="row"></div>
    <div class="row"><span class="section-title">Infectious Disease</span></div>
    <div class="row"><span class="label">Creutzfeldt-Jakob Disease</span><span class="options"><span class="opt"><span>Yes</span><i class="tick-box"></i></span><span class="opt"><span>No</span><i class="tick-box"></i></span></span></div>
    <div class="row"><span class="label">Hepatitis A,B,C,D</span><span class="options"><span class="opt"><span>Yes</span><i class="tick-box"></i></span><span class="opt"><span>No</span><i class="tick-box"></i></span></span></div>
  </div>

  <div class="column col-right">
    <div class="row"></div>
    <div class="row"><span class="label">HIV/AIDS</span><span class="options"><span class="opt"><span>Yes</span><i class="tick-box"></i></span><span class="opt"><span>No</span><i class="tick-box"></i></span></span></div>
    <div class="row"><span class="label">Influenza</span><span class="options"><span class="opt"><span>Yes</span><i class="tick-box"></i></span><span class="opt"><span>No</span><i class="tick-box"></i></span></span></div>
    <div class="row"><span class="label">Shingles</span><span class="options"><span class="opt"><span>Yes</span><i class="tick-box"></i></span><span class="opt"><span>No</span><i class="tick-box"></i></span></span></div>
    <div class="row"><span class="label">Tuberculosis</span><span class="options"><span class="opt"><span>Yes</span><i class="tick-box"></i></span><span class="opt"><span>No</span><i class="tick-box"></i></span></span></div>
    <div class="row"></div>
    <div class="row"><span class="section-title">Heart</span></div>
    <div class="row"><span class="label">Angina</span><span class="options"><span class="opt"><span>Yes</span><i class="tick-box"></i></span><span class="opt"><span>No</span><i class="tick-box"></i></span></span></div>
    <div class="row"><span class="label">Atrial Fibrillation</span><span class="options"><span class="opt"><span>Yes</span><i class="tick-box"></i></span><span class="opt"><span>No</span><i class="tick-box"></i></span></span></div>
    <div class="row"><span class="label">Blood Pressure (High/Low)</span><span class="options"><span class="opt"><span>Yes</span><i class="tick-box"></i></span><span class="opt"><span>No</span><i class="tick-box"></i></span></span></div>
    <div class="row"><span class="label">Congenital Heart Disease</span><span class="options"><span class="opt"><span>Yes</span><i class="tick-box"></i></span><span class="opt"><span>No</span><i class="tick-box"></i></span></span></div>
    <div class="row"><span class="label">Heart attack</span><span class="options"><span class="opt"><span>Yes</span><i class="tick-box"></i></span><span class="opt"><span>No</span><i class="tick-box"></i></span></span></div>
    <div class="row"><span class="label">Heart murmur</span><span class="options"><span class="opt"><span>Yes</span><i class="tick-box"></i></span><span class="opt"><span>No</span><i class="tick-box"></i></span></span></div>
    <div class="row"><span class="label">Heart surgery</span><span class="options"><span class="opt"><span>Yes</span><i class="tick-box"></i></span><span class="opt"><span>No</span><i class="tick-box"></i></span></span></div>
    <div class="row"><span class="label">Heart valve replacement</span><span class="options"><span class="opt"><span>Yes</span><i class="tick-box"></i></span><span class="opt"><span>No</span><i class="tick-box"></i></span></span></div>
    <div class="row"><span class="label">Infective endocarditis</span><span class="options"><span class="opt"><span>Yes</span><i class="tick-box"></i></span><span class="opt"><span>No</span><i class="tick-box"></i></span></span></div>
    <div class="row"><span class="label">Rheumatic Heart Disease</span><span class="options"><span class="opt"><span>Yes</span><i class="tick-box"></i></span><span class="opt"><span>No</span><i class="tick-box"></i></span></span></div>
    <div class="row"><span class="label">Pacemaker</span><span class="options"><span class="opt"><span>Yes</span><i class="tick-box"></i></span><span class="opt"><span>No</span><i class="tick-box"></i></span></span></div>
    <div class="row"><span class="label">Stent</span><span class="options"><span class="opt"><span>Yes</span><i class="tick-box"></i></span><span class="opt"><span>No</span><i class="tick-box"></i></span></span></div>
    <div class="row"></div>
    <div class="row"><span class="section-title">Other</span></div>
    <div class="row"><span class="label">Anxiety/PTSD</span><span class="options"><span class="opt"><span>Yes</span><i class="tick-box"></i></span><span class="opt"><span>No</span><i class="tick-box"></i></span></span></div>
    <div class="row"><span class="label">Arthritis</span><span class="options"><span class="opt"><span>Yes</span><i class="tick-box"></i></span><span class="opt"><span>No</span><i class="tick-box"></i></span></span></div>
    <div class="row"><span class="label">Alzheimer’s</span><span class="options"><span class="opt"><span>Yes</span><i class="tick-box"></i></span><span class="opt"><span>No</span><i class="tick-box"></i></span></span></div>
    <div class="row"><span class="label">Asthma</span><span class="options"><span class="opt"><span>Yes</span><i class="tick-box"></i></span><span class="opt"><span>No</span><i class="tick-box"></i></span></span></div>
    <div class="row"><span class="label">Anaphylaxis</span><span class="options"><span class="opt"><span>Yes</span><i class="tick-box"></i></span><span class="opt"><span>No</span><i class="tick-box"></i></span></span></div>
    <div class="row"><span class="label">Auto-immune disease</span><span class="options"><span class="opt"><span>Yes</span><i class="tick-box"></i></span><span class="opt"><span>No</span><i class="tick-box"></i></span></span></div>
    <div class="row"><span class="label">Coeliac</span><span class="options"><span class="opt"><span>Yes</span><i class="tick-box"></i></span><span class="opt"><span>No</span><i class="tick-box"></i></span></span></div>
    <div class="row"><span class="label">Depression</span><span class="options"><span class="opt"><span>Yes</span><i class="tick-box"></i></span><span class="opt"><span>No</span><i class="tick-box"></i></span></span></div>
    <div class="row"><span class="label">Diabetes</span><span class="options"><span class="opt"><span>Yes</span><i class="tick-box"></i></span><span class="opt"><span>No</span><i class="tick-box"></i></span></span></div>
    <div class="row"><span class="label">Epilepsy</span><span class="options"><span class="opt"><span>Yes</span><i class="tick-box"></i></span><span class="opt"><span>No</span><i class="tick-box"></i></span></span></div>
    <div class="row"><span class="label">Kidney Disease</span><span class="options"><span class="opt"><span>Yes</span><i class="tick-box"></i></span><span class="opt"><span>No</span><i class="tick-box"></i></span></span></div>
    <div class="row"><span class="label">Liver Disease</span><span class="options"><span class="opt"><span>Yes</span><i class="tick-box"></i></span><span class="opt"><span>No</span><i class="tick-box"></i></span></span></div>
    <div class="row"><span class="label">Osteoporosis</span><span class="options"><span class="opt"><span>Yes</span><i class="tick-box"></i></span><span class="opt"><span>No</span><i class="tick-box"></i></span></span></div>
    <div class="row"><span class="label">Parkinson’s</span><span class="options"><span class="opt"><span>Yes</span><i class="tick-box"></i></span><span class="opt"><span>No</span><i class="tick-box"></i></span></span></div>
    <div class="row"><span class="label">Radiation to Head/Neck</span><span class="options"><span class="opt"><span>Yes</span><i class="tick-box"></i></span><span class="opt"><span>No</span><i class="tick-box"></i></span></span></div>
    <div class="row"><span class="label">Schizophrenia</span><span class="options"><span class="opt"><span>Yes</span><i class="tick-box"></i></span><span class="opt"><span>No</span><i class="tick-box"></i></span></span></div>
    <div class="row"><span class="label">Snoring</span><span class="options"><span class="opt"><span>Yes</span><i class="tick-box"></i></span><span class="opt"><span>No</span><i class="tick-box"></i></span></span></div>
    <div class="row"><span class="label">Sleep apnea</span><span class="options"><span class="opt"><span>Yes</span><i class="tick-box"></i></span><span class="opt"><span>No</span><i class="tick-box"></i></span></span></div>
    <div class="row"><span class="label">Stroke</span><span class="options"><span class="opt"><span>Yes</span><i class="tick-box"></i></span><span class="opt"><span>No</span><i class="tick-box"></i></span></span></div>
  </div>

  <div class="other-line">Other:<span class="fill"></span></div>
  <div class="sign-line signature">Signature:<span class="fill"></span></div>
  <div class="sign-line date">Date:<span class="fill"></span></div>

  <footer class="footer">
    <p>Thank you for the time to complete your medical history form.</p>
    <p>Oral health is linked to overall health and this comprehensive questionnaire will help us to provide you with optimal and safe care.</p>
  </footer>
</body>
</html>
```